New Business Cards for MB&LR

We need updated business cards for a staff of 15 engineers, estimators, project managers, and sales people. We have recently begun changes to our website and marketing material to improve our look and branding. We are an established fabricator specializing in pressure vessels, tanks, and structural steel. The owners require us to use the existing logo and old english text design. Also, we prefer dark grey or mostly black cards.
Target Market(s)
Engineers, purchasing agents, estimators, and project managers of; mining companies, refineries, industrial construction professionals
Industry/Entity Type
Business
Contact Information for Business Card
Logo, phone, website, email, etc.
Look and feel

```html
<!DOCTYPE html>
<html lang="en">
<head>
<meta charset="utf-8">
<title>MB&amp;LR Business Card</title>
<link rel="stylesheet" href="https://fonts.googleapis.com/css2?family=Roboto:wght@400;500;700&family=Roboto+Condensed:wght@700&display=swap">
<style>
  :root {
    --stage: #6f4d33;
    --card-light: #f3f3f3;
    --card-dark: #1b1c1e;
    --ink: #1e1e1e;
    --ink-soft: #3c3c3c;
    --ink-muted: #9a9a9a;
    --rule: #9c9c9c;
    --paper-white: #f5f5f5;
  }
  * { margin: 0; padding: 0; box-sizing: border-box; }
  html, body { width: 1200px; height: 960px; overflow: hidden; }
  body {
    background: var(--stage);
    position: relative;
    font-family: "Roboto", Arial, sans-serif;
  }
  .card {
    position: absolute;
    width: 600px;
    box-shadow: 0 4px 10px rgba(0,0,0,0.35);
  }
  .card--front {
    left: 314px; top: 113px; height: 324px;
    background: var(--card-light);
    color: var(--ink);
  }
  .card--back {
    left: 312px; top: 472px; height: 343px;
    background: var(--card-dark);
    color: var(--paper-white);
  }
  .brand {
    position: absolute;
    display: flex;
    align-items: center;
    gap: 10px;
    font-family: "Roboto", Arial, sans-serif;
    font-weight: 700;
  }
  .card--front .brand {
    left: 80px; top: 142px;
    font-size: 34px;
    color: var(--ink);
  }
  .brand__square {
    width: 16px; height: 16px;
    background: currentColor;
  }
  .divider {
    position: absolute;
    left: 305px; top: 88px;
    width: 1px; height: 170px;
    background: var(--rule);
  }
  .contact {
    position: absolute;
    left: 340px; top: 90px;
  }
  .contact__name {
    font-family: "Roboto Condensed", "Arial Narrow", sans-serif;
    font-weight: 700;
    font-size: 20px;
    letter-spacing: 0.2px;
    color: var(--ink);
  }
  .contact__title {
    font-size: 14px;
    color: var(--ink-muted);
    margin-top: 2px;
  }
  .contact__address {
    font-size: 14px;
    line-height: 18px;
    color: var(--ink-soft);
    margin-top: 14px;
  }
  .contact__lines {
    list-style: none;
    margin-top: 10px;
    font-size: 14px;
    line-height: 19px;
    color: var(--ink-soft);
  }
  .contact__lines li { display: flex; align-items: center; gap: 8px; }
  .contact__lines svg { width: 14px; height: 14px; fill: var(--ink); }
  .card--back .brand {
    left: 0; right: 0; top: 130px;
    justify-content: center;
    font-size: 44px;
    color: var(--paper-white);
  }
  .company-name {
    position: absolute;
    left: 0; right: 0; top: 228px;
    text-align: center;
    font-size: 21px;
    font-weight: 500;
    color: var(--paper-white);
  }
  .web {
    position: absolute;
    left: 0; right: 0; top: 264px;
    text-align: center;
    font-size: 13px;
    letter-spacing: 6px;
    color: var(--paper-white);
  }
</style>
</head>
<body>
  <section class="card card--front">
    <div class="brand"><span class="brand__square"></span>MB&amp;LR</div>
    <div class="divider"></div>
    <div class="contact">
      <p class="contact__name">DANIEL REEVE</p>
      <p class="contact__title">CEO/FOUNDER</p>
      <p class="contact__address">410 East 200 South<br>Granite Falls City 84190</p>
      <ul class="contact__lines">
        <li>
          <svg viewBox="0 0 24 24" aria-hidden="true"><path d="M6.6 10.8a15.1 15.1 0 0 0 6.6 6.6l2.2-2.2c.3-.3.7-.4 1-.2 1.1.4 2.3.6 3.6.6.6 0 1 .4 1 1V20c0 .6-.4 1-1 1C10.6 21 3 13.4 3 4c0-.6.4-1 1-1h3.5c.6 0 1 .4 1 1 0 1.3.2 2.5.6 3.6.1.3 0 .7-.2 1z"/></svg>
          555.318.2047
        </li>
        <li>
          <svg viewBox="0 0 24 24" aria-hidden="true"><path d="M6 2h12v6H6zM3 9h18a1 1 0 0 1 1 1v8h-4v4H6v-4H2v-8a1 1 0 0 1 1-1zm5 7v4h8v-4z"/></svg>
          555.318.2099
        </li>
        <li>
          <svg viewBox="0 0 24 24" aria-hidden="true"><path d="M12 2a10 10 0 1 0 0 20 10 10 0 0 0 0-20zm-1 17.9A8 8 0 0 1 4.1 10l4.9 5v1a2 2 0 0 0 2 2zm6.9-2.5A2 2 0 0 0 16 16h-1v-3a1 1 0 0 0-1-1H8v-2h2a1 1 0 0 0 1-1V7h2a2 2 0 0 0 2-2v-.4a8 8 0 0 1 2.9 12.8z"/></svg>
          www.mbandlr.com
        </li>
      </ul>
    </div>
  </section>

  <section class="card card--back">
    <div class="brand"><span class="brand__square"></span>MB&amp;LR</div>
    <p class="company-name">Midland Boiler &amp; Liner Rolling</p>
    <p class="web">www.mbandlr.com</p>
  </section>
</body>
</html>
```